Luxurious Rustic Cottage Accommodation brochure design

I would like a trifold brochure design to continue the theme I already have established on my website www.atbellowvale.com.au The basic theme uses the logo from the website, it is called "At Dunforths" B & B Private Cottages and has black background with use of gold for borders and highlights. The accommodation is in the hinterland region of the Sunshine Coast, Queensland, Australia. I have 4 separate private cottages which I would like to include information & pictures about each as per details on the website mentioned. Features to highlight include ocean views, log fires, spa baths, romance, nature. Accommodation is suitable for couples, family, small group or wedding party, special occasion getways. Package inclusions to be highlighted are breakfast hamper, complimentary chocolates & champagne, pamper products, optional inclusions are cheese platter, relaxation massage. I would like location to be included by way of a map, contact details (website, email & mobile phone) to also be included.
There are pictures on the website which I can provide high resolution for brochure printing as required. Some more images have been uploaded for optional use.

```html
<!DOCTYPE html>
<html lang="en">
<head>
<meta charset="utf-8">
<title>At Dunforths – Private Cottages Brochure</title>
<link rel="stylesheet" href="https://fonts.googleapis.com/css2?family=Arimo:wght@400&family=Questrial&display=swap">
<style>
  :root {
    --bg: #0b0b0c;
    --panel: #1b1c1e;
    --panel-light: #2a2b2e;
    --gold: #9a6f14;
    --gold-text: #a9802f;
    --accent: #c3dc3a;
    --body-text: #e6e6e6;
    --sky-top: #7fb6e6;
    --sky-bottom: #d9ecf6;
    --tree: #5f8a3a;
    --cloth: #cdd8e6;
  }
  * { margin: 0; padding: 0; box-sizing: border-box; }
  html, body { width: 1200px; height: 933px; overflow: hidden; background: var(--bg); }
  .brochure {
    position: relative; width: 1200px; height: 933px; overflow: hidden;
    background:
      linear-gradient(180deg, rgba(40,41,44,.55) 0%, rgba(20,20,22,0) 40%),
      var(--bg);
    font-family: "Arimo", Arial, sans-serif;
  }
  .shade { position: absolute; background: var(--panel); }
  .shade--top { left: 0; top: 0; width: 685px; height: 48px; background: #26272a; }
  .shade--left { left: 0; top: 520px; width: 430px; height: 380px; background: #141416; }
  .shade--mid { left: 430px; top: 150px; width: 370px; height: 380px; background: #121214; }
  .gold-rule { position: absolute; left: 0; width: 1200px; height: 5px; background: var(--gold); }
  .gold-rule--top { top: 46px; }
  .gold-rule--bottom { top: 893px; }
  .photo { position: absolute; }
  .photo--balcony {
    left: 102px; top: 66px; width: 464px; height: 462px;
    background: linear-gradient(180deg, var(--sky-top) 0%, var(--sky-bottom) 55%, var(--tree) 62%, #3f5f2c 78%, var(--cloth) 100%);
  }
  .frame { position: absolute; background: var(--panel-light); }
  .frame--spa { left: 617px; top: 210px; width: 259px; height: 215px; }
  .photo--spa {
    left: 640px; top: 241px; width: 233px; height: 168px;
    background: linear-gradient(160deg, #6b7a6a 0%, #e8eef0 45%, #f7f7f5 70%, #b9b29a 100%);
  }
  .frame--lodge { left: 796px; top: 537px; width: 404px; height: 356px; background: #222326; }
  .photo--lodge {
    left: 839px; top: 668px; width: 308px; height: 207px;
    background: linear-gradient(180deg, #eef3f5 0%, #cfe0e8 30%, var(--tree) 45%, #3d4a3a 65%, var(--cloth) 85%, #f2f4f6 100%);
  }
  .text-block { position: absolute; font-size: 12.8px; line-height: 21.7px; color: var(--body-text); }
  .text-block p + p { margin-top: 21.7px; }
  .heading {
    font-family: "Questrial", "Century Gothic", sans-serif; font-weight: 400;
    font-size: 21px; line-height: 26px; color: var(--accent); margin-bottom: 2px;
  }
  .intro { left: 103px; top: 561px; width: 278px; color: var(--gold-text); }
  .about { left: 433px; top: 472px; width: 345px; }
  .cottage--drovers { left: 822px; top: 62px; width: 352px; }
  .cottage--wattlewood { left: 888px; top: 223px; width: 292px; }
  .cottage--kirralee { left: 822px; top: 410px; width: 352px; }
  .cottage--lodge { left: 822px; top: 545px; width: 350px; }
</style>
</head>
<body>
<main class="brochure">
  <div class="shade shade--top"></div>
  <div class="shade shade--mid"></div>
  <div class="shade shade--left"></div>
  <div class="gold-rule gold-rule--top"></div>

  <div class="photo photo--balcony" role="img" aria-label="Balcony table with wine glasses and a platter overlooking the hinterland and ocean"></div>

  <section class="text-block intro">
    <p>Luxurious Rustic Cabin &amp; Lodge Accommodation in Montville, Queensland At Dunforth’s private cottages in Montville boasts one of the best panoramic views to the ocean, we have 3 separate private cabins to accommodate couples and a 4 bedroom Lodge to accommodate up to 8 guests.</p>
    <p>Situated on the historical “Dunforth’s Shute” just 2 kms from the quaint Montville township, "At Dunforths" is an ideal location to relax and enjoy the Sunshine Coast Hinterland. Approximately one and a half hours drive north of Brisbane and just a few minutes from the beautiful villages of Montville &amp; Maleny.</p>
  </section>

  <section class="text-block about">
    <h2 class="heading">About Us</h2>
    <p>In 1887, the first settlers came to Montville and started clearing the land, “Shutes” such as Dunforths were used to slide the huge logs down the mountain to Bullock teams waiting at the bottom.</p>
    <p>Today, the wheel has turned from farming to tourism and “Dunforth’s Shute” is now the site of our luxurious guest accommodation, revegetated with native &amp; rainforest trees and alive with wildlife including possums and an array of birds.</p>
    <p>Our accommodation buildings were inspired by our history and built using a “rustic theme”, recycled timbers and a design that replicates that of the early settlers cottages, they were completed in 2009.</p>
    <p>Our future includes plans to open a walking track along the shute for our guests to explore &amp; enjoy …</p>
  </section>

  <section class="text-block cottage--drovers">
    <h2 class="heading">Drovers Song</h2>
    <p>Rustic luxurious king size bed, indoor/outdoor spa bath set amongst the treetops with magical views overlooking the hinterland and beyond. Awake to the sound of birds and magnificent sunrises, fresh air on your private balcony or throw a log on the fire to create an intimate atmosphere.</p>
  </section>

  <div class="frame frame--spa"></div>
  <div class="photo photo--spa" role="img" aria-label="Bubble-filled spa bath with a glass of champagne"></div>

  <section class="text-block cottage--wattlewood">
    <h2 class="heading">Wattlewood</h2>
    <p>Surrounded by fragrant timber, featuring hand crafted camphor furniture. Set amongst tall trees and nature with a panoramic hinterland &amp; ocean view. Misty mornings &amp; crystal clear afternoons are scenes to enjoy from the spa bath, balcony or comfy couches by the log fire. All you need for romance or to relax, revive &amp; reminisce.</p>
  </section>

  <section class="text-block cottage--kirralee">
    <h2 class="heading">Kirralee</h2>
    <p>A luxurious escape for a couple or small family, featuring a king size bed with an option to add two single beds, a private &amp; self contained setting, hinterland &amp; coastal views, spa bath &amp; log fire. Enjoy the birds singing &amp; stunning sunrises.</p>
  </section>

  <div class="frame frame--lodge"></div>
  <section class="text-block cottage--lodge">
    <h2 class="heading">Lodge</h2>
    <p>Our Lodge accommodation features 4 bedrooms and a great open plan living space with ocean &amp; hinterland views from every aspect. An ideal gathering spot or retreat for family &amp; friends.</p>
  </section>
  <div class="photo photo--lodge" role="img" aria-label="Balcony table set for two with hinterland views beyond"></div>

  <div class="gold-rule gold-rule--bottom"></div>
</main>
</body>
</html>
```